Moderne CI für einen Immobilienmakler [www.terbek-wohnwerte.de]
Zielgruppe
Kunden für hochwertige Immobilien, also gemischtes eher anspruchvolles Klientel.
Hallo,
ich betreibe ein junges Immobilienunternehmen im 4. Geschäftsjahr. Wir vermarkten ausschließlich hochwertige Immobilien. Meine derzeitiges Logo habe ich damals selbst entworfen und es harmoniert gut mit meiner Website [www.terbek-wohnwerte.de] leider habe ich für Printmedien nie eine CI hinbekommen die mir richtig gefällt und die im Gesamt- und Farbkonzept zu meinem Onlineauftritt passt.
Ich wünsche mir nun von einem professionellen Designer eine modern- edle CI mit Entwürfen für Briefpapier, Umschläge C4 und DL, A4 Exposé-Mappe sowie die Rohlinge für eine Dreiseiter Image-Broschüre, für ein Objekt Expose sowie für eine Print-Annonce.
Eine spätere Zusammenarbeit für weitere Medien ist erwünscht.

```html
<!DOCTYPE html>
<html lang="de">
<head>
<meta charset="utf-8">
<title>Terbek Wohnwerte – Objekt-Exposé</title>
<link href="https://fonts.googleapis.com/css2?family=Open+Sans:wght@400;600;700&display=swap" rel="stylesheet">
<style>
  :root {
    --red: #c41a34;
    --red-dark: #8e0f2c;
    --maroon: #6e0f2a;
    --grey-text: #6d6d6d;
    --grey-dark: #3d3d3d;
    --grey-cell: #d4d4d4;
    --grey-cell-light: #e8e8e8;
    --paper: #ffffff;
  }
  * { margin: 0; padding: 0; box-sizing: border-box; }
  html, body { width: 871px; height: 1200px; overflow: hidden; background: #ffffff; }
  body { font-family: "Open Sans", Arial, sans-serif; color: var(--grey-text); }
  .sheet { position: relative; width: 871px; height: 1200px; background: var(--paper); overflow: hidden; }

  .masthead { position: absolute; left: 0; top: 0; width: 871px; height: 77px; border-bottom: 4px solid var(--red); }
  .brand { position: absolute; left: 36px; top: 16px; font-size: 38px; font-weight: 400; color: #8a8a8a; letter-spacing: 0.5px; }

  .hero { position: absolute; left: 0; top: 77px; width: 871px; height: 322px; display: flex; border-bottom: 5px solid var(--grey-dark); }
  .hero-facade { width: 358px; height: 100%; background: linear-gradient(135deg, #a08a74 0%, #c9b8a4 45%, #5c5248 70%, #8e7e6c 100%); }
  .hero-house { flex: 1; height: 100%; background: linear-gradient(180deg, #9fb3c8 0%, #d7dde2 40%, #c4ab8c 62%, #7b8a56 82%, #5e7040 100%); }
  .tagline { position: absolute; right: 26px; top: 60px; background: var(--red); color: #fff; font-size: 22px; font-weight: 600; padding: 6px 22px 7px; border: 2px solid #fff; }

  .intro { position: absolute; left: 36px; top: 450px; width: 476px; }
  .section-title { color: var(--red); font-size: 17px; font-weight: 600; margin-bottom: 12px; }
  .body-copy { font-size: 13.5px; line-height: 20px; text-align: justify; color: var(--grey-text); letter-spacing: 0.2px; }

  .contact-person { position: absolute; left: 36px; top: 744px; width: 476px; }

  .facts { position: absolute; left: 540px; top: 448px; width: 305px; }
  .facts-title { font-size: 17px; color: var(--grey-dark); text-align: right; margin-bottom: 10px; }
  .facts-title span { color: var(--grey-text); }
  .facts-table { width: 100%; border-collapse: collapse; font-size: 13.5px; }
  .facts-table th { width: 150px; text-align: right; font-weight: 400; color: var(--grey-dark); padding: 0 10px; height: 38px; }
  .facts-table td { padding: 0 12px; color: var(--grey-dark); }
  .facts-table tr:nth-child(odd) th, .facts-table tr:nth-child(odd) td { background: var(--grey-cell); }
  .facts-table tr:nth-child(even) th { background: var(--grey-cell-light); }
  .facts-table tr:nth-child(even) td { background: #fff; }
  .facts-photo { margin-top: 14px; margin-left: 5px; width: 300px; height: 160px; background: linear-gradient(180deg, #aab8c6 0%, #d0d3d2 40%, #b59c7f 60%, #6f7b4c 85%, #546035 100%); }

  .footer { position: absolute; left: 0; top: 1090px; width: 871px; height: 110px; display: flex; color: #fff; font-size: 13.5px; line-height: 19px; }
  .footer-main { width: 620px; background: linear-gradient(90deg, var(--red) 0%, var(--red-dark) 100%); display: flex; padding: 18px 0 0 36px; }
  .footer-col { width: 280px; }
  .footer-col strong { font-weight: 700; }
  .footer-side { flex: 1; background: var(--maroon); padding: 18px 20px 0 28px; font-weight: 600; }
</style>
</head>
<body>
<div class="sheet">
  <header class="masthead">
    <div class="brand">terbek wohnwerte</div>
  </header>

  <section class="hero">
    <div class="hero-facade" role="img" aria-label="Detailansicht der Holzfassade mit Eckfenster"></div>
    <div class="hero-house" role="img" aria-label="Außenansicht des modernen Hauses mit Holzfassade und Garten"></div>
  </section>
  <div class="tagline">Idyllisch modern Wohnen</div>

  <section class="intro">
    <h2 class="section-title">Ihre zukünftige Eigentumswohnung</h2>
    <p class="body-copy">Lorem ipsum dolor sit amet, consectetur adipiscing elit. Sed quam eros, dapibus et dictum quis, tincidunt et nibh. In hac habitasse platea dictumst. Maecenas euismod commodo blandit. Suspendisse potenti. Curabitur vestibulum, urna eu luctus sagittis, metus erat auctor arcu, vel posuere erat eros eu leo. Nulla facilisi. Nam ornare sagittis enim, venenatis cursus magna suscipit et. Vivamus gravida convallis urna, et convallis nulla hendrerit id. Morbi nibh magna, dignissim at ullamcorper ac, vehicula facilisis lorem. Pellentesque leo lorem, imperdiet et semper at, rutrum eu tellus.</p>
  </section>

  <section class="contact-person">
    <h2 class="section-title">Ihr Ansprechpartner</h2>
    <p class="body-copy">Lorem ipsum dolor sit amet, consectetur adipiscing elit. Sed quam eros, dapibus et dictum quis, tincidunt et nibh. In hac habitasse platea dictumst. Maecenas euismod commodo blandit. Suspendisse potenti. Curabitur vestibulum, urna eu luctus sagittis, metus erat auctor arcu, vel posuere erat eros eu leo. Nulla facilisi.</p>
  </section>

  <aside class="facts">
    <h2 class="facts-title">Objektbezogene <span>Daten</span></h2>
    <table class="facts-table">
      <tr><th>Kaufpreis:</th><td>175.000,00 €</td></tr>
      <tr><th>Hausgeld:</th><td>210,00 €</td></tr>
      <tr><th>Zimmer:</th><td>5</td></tr>
      <tr><th>Badezimmer:</th><td>1</td></tr>
      <tr><th>Schlafzimmer:</th><td>2</td></tr>
      <tr><th>Wohnfläche:</th><td>150 qm</td></tr>
      <tr><th>Baujahr:</th><td>2008</td></tr>
      <tr><th>Verfügbar ab:</th><td>sofort</td></tr>
    </table>
    <div class="facts-photo" role="img" aria-label="Gesamtansicht des Hauses am Hang"></div>
  </aside>

  <footer class="footer">
    <div class="footer-main">
      <div class="footer-col">
        <strong>Terbek Wohnwerte</strong><br>
        Inhaber: Henrik Terbek<br>
        Lindenweg 14<br>
        35039 Musterstadt
      </div>
      <div class="footer-col">
        <strong>Kontaktmöglichkeiten</strong><br>
        Telefon: 06421-550 2710<br>
        Telefax: 06421-550 2712<br>
        Mobil: 0172-908337 204
      </div>
    </div>
    <div class="footer-side">
      info@terbek-wohnwerte.de<br>
      www.terbek-wohnwerte.de
    </div>
  </footer>
</div>
</body>
</html>
```